25kg bag for branded milk powder

We are looking for an attractive bag for our Holland dairy milk powder range. We will have 5 kinds of products.

Instant Full Cream milk powder
Full cream milk powder
Instant fat filled milk powder
Skimmed milk powder
Dairy ingredients

The bags are standard industrial 25kg kraft multiply paper bags with inner poly linner.

We want to have an hormonized design where each type of dairy product is differentiated by the product name and a color,

Please see attached design as reference.

Target Market(s)

Middle East and Africa

Font styles to use
Sans Serif

Requirements
Must have
• The bags must show that we are a dutch company and have a profesional feel.
• We want a general design that will be differentiated by colour coding.
• We want the design to be less conservative compared to the attached examples.
• The bags must be easilly recognisable from all sides as for picture of Vorlund Creameries branded bags on pallets attached.
• We have also attached some bags design templates as a reference.
Nice to have
• We would like to use sybols or imagery that symbolises Dutch origin and quality
Should not have
• We cannot have too many images to keep it simple.

```html
<!DOCTYPE html>
<html lang="en">
<head>
<meta charset="utf-8">
<title>Veldmark Dairy Foods – 25kg Milk Powder Bag Layout</title>
<link href="https://fonts.googleapis.com/css2?family=Open+Sans:wght@700&family=PT+Sans:wght@700&display=swap" rel="stylesheet">
<style>
  :root {
    --brand-yellow: #fcc23e;
    --brand-yellow-soft: #fdd27a;
    --paper: #ffffff;
    --fold-line: #4a4a4a;
    --flap-text: #ffffff;
  }
  html, body {
    margin: 0;
    padding: 0;
    width: 1200px;
    height: 1052px;
    overflow: hidden;
    background: var(--paper);
  }
  .bag-layout {
    display: block;
    width: 1200px;
    height: 1052px;
  }
  .panel-bg { fill: var(--paper); }
  .band { fill: var(--brand-yellow); }
  .fold { stroke: var(--fold-line); stroke-width: 0.8; fill: none; }
  .outline { stroke: #222; stroke-width: 1; fill: none; }
  .brand-name {
    font-family: "Open Sans", Arial, sans-serif;
    font-weight: 700;
    fill: var(--brand-yellow);
  }
  .brand-sub { letter-spacing: 5px; }
  .flap .brand-name { fill: var(--flap-text); }
  .product-name, .product-weight {
    font-family: "PT Sans", Arial, sans-serif;
    font-weight: 700;
    fill: var(--brand-yellow);
  }
</style>
</head>
<body>
<svg class="bag-layout" viewBox="0 0 1200 1052" xmlns="http://www.w3.org/2000/svg">
  <defs>
    <linearGradient id="sceneTone" x1="0" y1="0" x2="0" y2="1">
      <stop offset="0" stop-color="#fcc23e" stop-opacity="0.15"/>
      <stop offset="0.6" stop-color="#fcc23e" stop-opacity="0.75"/>
      <stop offset="1" stop-color="#fcc23e" stop-opacity="1"/>
    </linearGradient>
  </defs>

  <!-- bag body -->
  <rect class="panel-bg" x="6" y="6" width="1188" height="902"/>
  <polygon class="band band-top" points="6,6 1194,6 1194,328 6,14"/>
  <polygon class="band band-bottom" points="6,682 848,908 6,908"/>

  <!-- front scene area -->
  <rect class="front-scene" x="208" y="624" width="434" height="284" fill="url(#sceneTone)"
        role="img" aria-label="Dutch countryside scene with a farmhouse and a windmill beside a small bridge, in yellow tones"/>

  <!-- front panel -->
  <g class="front-panel">
    <text class="brand-name" x="418" y="272" font-size="54" text-anchor="middle">VELDMARK</text>
    <text class="brand-name brand-sub" x="420" y="314" font-size="30" text-anchor="middle">Dairy Foods</text>
    <text class="product-name" x="424" y="403" font-size="30" text-anchor="middle">Instant Full Cream</text>
    <text class="product-name" x="424" y="444" font-size="30" text-anchor="middle">Milk Powder</text>
    <text class="product-weight" x="424" y="551" font-size="50" text-anchor="middle">25kg</text>
  </g>

  <!-- left gusset -->
  <g class="gusset gusset-left">
    <text class="brand-name" transform="translate(140 440) rotate(90)" font-size="50" text-anchor="middle">VELDMARK</text>
    <text class="brand-name brand-sub" transform="translate(90 452) rotate(90)" font-size="30" text-anchor="middle">Dairy Foods</text>
  </g>

  <!-- right gusset -->
  <g class="gusset gusset-right">
    <text class="brand-name" transform="translate(714 462) rotate(-90)" font-size="50" text-anchor="middle">VELDMARK</text>
    <text class="brand-name brand-sub" transform="translate(756 452) rotate(-90)" font-size="30" text-anchor="middle">Dairy Foods</text>
  </g>

  <!-- fold lines -->
  <g class="folds">
    <line class="fold" x1="27" y1="6" x2="27" y2="908"/>
    <line class="fold" x1="58" y1="6" x2="58" y2="908"/>
    <line class="fold" x1="133" y1="6" x2="133" y2="908"/>
    <line class="fold" x1="207" y1="6" x2="207" y2="908"/>
    <line class="fold" x1="642" y1="6" x2="642" y2="908"/>
    <line class="fold" x1="717" y1="6" x2="717" y2="908"/>
    <line class="fold" x1="791" y1="6" x2="791" y2="908"/>
  </g>
  <rect class="outline" x="6" y="6" width="1188" height="902"/>

  <!-- bottom flap -->
  <g class="flap">
    <rect class="band" x="207" y="908" width="435" height="138"/>
    <rect class="outline" x="207" y="908" width="435" height="138"/>
    <text class="brand-name" x="420" y="983" font-size="42" text-anchor="middle">VELDMARK</text>
    <text class="brand-name brand-sub" x="422" y="1012" font-size="24" text-anchor="middle">Dairy Foods</text>
  </g>
</svg>
</body>
</html>
```